Brightwater Court Services needs a business card

I need a business card design for a new company
For the last 10 years I have ran a tennis management company called Silver Hollow Racquet (www.silverhollowracquet.com)
The new company - Brightwater Court Services (BCS) will replace SHRA starting this winter
The goal of BCS will be to expand our operations into new clubs as well and a revenue stream from existing clubs with courtlinkhub.net
We plan to go regional in 2014 and then look outward from there

Target Market(s)

small to medium sized tennis facilities both public and private
Our market are the clubs - not the players
This includes private clubs, municipalities, recreation assc, etc

Industry/Entity Type

Business

Requirements
Must have
• Dale Huxley
• President
• 555-284-1937 Office
• 555-419-5062 Cell
• dhuxley@brightwatercourtservices.com
• www.brightwatercourtservices.com
Nice to have
• One of the unique benefits to a company joining BCS will be integration into our web based club software service - Courtlinkhub.net
• We have developed this turnkey service for small to medium sized clubs and re the exclusive providers of it
Should not have
• address or state

```html
<!DOCTYPE html>
<html lang="en">
<head>
<meta charset="utf-8">
<title>Brightwater Court Services — Business Card</title>
<link rel="stylesheet" href="https://fonts.googleapis.com/css2?family=Arimo:wght@400;700&display=swap">
<style>
  :root {
    --court-dark: #1f2b22;
    --court-mid: #2f5a3c;
    --court-light: #3f6e4c;
    --ball-tone: #c9dc3a;
    --band-white: #f7f7f5;
    --ink-green: #2e4a2b;
    --text-white: #ffffff;
    --text-soft: #e6eee4;
  }
  * { margin: 0; padding: 0; box-sizing: border-box; }
  html, body {
    width: 1200px;
    height: 686px;
    overflow: hidden;
    background: var(--court-mid);
  }
  .card {
    position: relative;
    width: 1200px;
    height: 686px;
    overflow: hidden;
    font-family: "Arimo", Arial, sans-serif;
  }
  .court-photo {
    position: absolute;
    inset: 0;
    background:
      radial-gradient(circle at 905px 390px, rgba(201,220,58,0.95) 0, rgba(201,220,58,0.55) 150px, transparent 200px),
      linear-gradient(180deg, var(--court-dark) 0%, #2c3d30 28%, var(--court-mid) 45%, var(--court-light) 100%);
  }
  .club-mark {
    position: absolute;
    left: 136px;
    top: 412px;
    display: flex;
    align-items: center;
    gap: 14px;
  }
  .club-mark__dot {
    width: 30px;
    height: 30px;
    border-radius: 50%;
    background: var(--text-white);
  }
  .club-mark__name {
    color: var(--text-white);
    font-size: 50px;
    font-weight: 700;
    letter-spacing: -1px;
    line-height: 1;
  }
  .contact {
    position: absolute;
    left: 138px;
    top: 486px;
    color: var(--text-soft);
    line-height: 1;
  }
  .contact__name {
    color: var(--text-white);
    font-size: 24px;
    font-weight: 700;
    margin-bottom: 12px;
  }
  .contact__role {
    font-weight: 400;
    color: var(--text-soft);
  }
  .contact__line {
    font-size: 18px;
    font-weight: 400;
    margin-bottom: 9px;
  }
  .url-band {
    position: absolute;
    left: 25px;
    top: 594px;
    width: 1147px;
    height: 130px;
    border-radius: 46px 46px 0 0;
    background: var(--band-white);
  }
  .url-band__text {
    position: absolute;
    left: 0;
    right: 0;
    top: 30px;
    text-align: center;
    color: var(--ink-green);
    font-size: 40px;
    font-weight: 700;
    letter-spacing: 5px;
    line-height: 1;
  }
</style>
</head>
<body>
  <div class="card">
    <div class="court-photo" role="img" aria-label="Photo of a tennis ball resting on a white court line with the net blurred behind"></div>

    <div class="club-mark">
      <span class="club-mark__dot"></span>
      <span class="club-mark__name">courtlinkhub</span>
    </div>

    <div class="contact">
      <p class="contact__name">Dale Huxley <span class="contact__role">· President</span></p>
      <p class="contact__line">555-284-1937 Office &nbsp;|&nbsp; 555-419-5062 Cell</p>
      <p class="contact__line">dhuxley@brightwatercourtservices.com</p>
    </div>

    <div class="url-band">
      <p class="url-band__text">www.brightwatercourtservices.com</p>
    </div>
  </div>
</body>
</html>
```